Brochure for Charter Boat

We require a brochure for a new charter boat business, called Reelside Tides Bayvale, We do Fishing Charters, Corbett Reef Nature Cruises, Diving, and Whale Watching tour.

Corbett Reef Nature Cruises - Lighthouse, seals.

We offer refreshments on all our charters and lunch is provided on a full day fishing charter.

We are waiting on photos. but have included some photos, I can change photos later. Would like to put a photo of the boat in, but still waiting to receive it from photographer.

www.reelsidetidesbayvale.example (currently changing website, just purchased design from artbazaar).
Updates

Project Deadline Extended
Reason: getting a logo designed by artbazaar, so I can add logo to brochure. Thank you!

Project Deadline Extended
Reason: As I haven't provided information and now have a logo which was desinged by ArtBazaar.

Target Market(s)

Fisherman and Families

Industry/Entity Type

Business

Requirements
Must have
• Phone number, website, business Name - Reelside Tides Bayvale and logo. Please include 'specalising in Small Groups'

Photo of boat, (which I'm waiting on at the moment)
Nice to have
• 1/2 Day fishing $150 per person - 5 hours, refreshments provided. Includes all fishing tackle & bait.
Full Day Fishing $250 per person - 9 hours, Lunch and refreshments provided. Includes all fishing tackle & bait
2 Hour Fish - $80 per person, drinks provided and all fishing tackle & bait
4 hour Morning Corbett Nature Cruise - $120 per person, refreshments provided
3 hour Afternoon Corbett Nature Cruise - $100 per person, refreshments provided.
Vessel: 9.8 meter custom built plate aluminium.
Whale watching from September to November

```html
<!DOCTYPE html>
<html lang="en">
<head>
<meta charset="utf-8">
<title>Reelside Tides Bayvale – Trifold Brochure</title>
<link rel="stylesheet" href="https://fonts.googleapis.com/css2?family=Delius&family=Open+Sans:wght@400&display=swap">
<style>
  :root {
    --sea: #1b6894;
    --sea-line: #2f7aa3;
    --paper: #ffffff;
    --ink: #111111;
    --fold: #c8866a;
    --photo-sky: #6f8fa8;
    --photo-water: #2c4f6a;
  }
  * { margin: 0; padding: 0; box-sizing: border-box; }
  html, body { width: 1200px; height: 472px; overflow: hidden; background: var(--paper); }
  body { position: relative; font-family: "Delius", "Comic Neue", sans-serif; color: var(--paper); }

  .side-label { position: absolute; top: 0; font-family: "Open Sans", sans-serif; font-size: 20px; color: var(--ink); letter-spacing: 0.5px; }
  .side-label--front { left: 251px; }
  .side-label--back { left: 882px; }

  .fold-mark { position: absolute; width: 0; height: 22px; border-left: 1px dashed var(--fold); }
  .fold-mark--top { top: 8px; }
  .fold-mark--bottom { top: 447px; }

  .sheet { position: absolute; top: 37px; height: 409px; background: var(--sea); display: flex; }
  .sheet--front { left: 0; width: 579px; }
  .sheet--back { left: 620px; width: 580px; }

  .panel { position: relative; width: 193px; height: 100%; border-left: 1px solid var(--sea-line); text-align: center; }
  .panel:first-child { border-left: none; }

  .rule { position: absolute; height: 4px; background: var(--paper); }

  .panel-heading { position: absolute; left: 0; right: 0; font-weight: 400; line-height: 1.12; }
  .body-copy { position: absolute; left: 4px; right: 4px; font-size: 8.6px; line-height: 11.2px; }

  .photo { position: absolute; background: linear-gradient(180deg, var(--photo-sky) 0%, var(--photo-water) 55%, #1f3a4e 100%); }

  /* welcome */
  .welcome-heading { top: 24px; font-size: 13.5px; }
  .welcome-copy { top: 71px; }

  /* fishing */
  .fishing-title { top: 16px; font-size: 31px; }
  .fishing-copy { top: 76px; font-size: 8.8px; }
  .fishing-prices { position: absolute; top: 346px; left: 0; right: 0; font-size: 12px; line-height: 14.5px; }

  /* cruises */
  .cruise-heading { top: 22px; font-size: 14px; }
  .tour-title { position: absolute; left: 0; right: 0; font-size: 8.6px; }
  .cruise-copy { font-size: 8.3px; line-height: 11px; }

  /* back cover */
  .cover-title { top: 28px; font-size: 28px; line-height: 1.18; }

  /* contact */
  .contact-block { position: absolute; left: 0; right: 0; font-size: 11px; line-height: 14px; }
</style>
</head>
<body>
  <div class="side-label side-label--front">FRONT</div>
  <div class="side-label side-label--back">BACK</div>

  <div class="fold-mark fold-mark--top" style="left:193px"></div>
  <div class="fold-mark fold-mark--top" style="left:386px"></div>
  <div class="fold-mark fold-mark--top" style="left:813px"></div>
  <div class="fold-mark fold-mark--top" style="left:1006px"></div>
  <div class="fold-mark fold-mark--bottom" style="left:193px"></div>
  <div class="fold-mark fold-mark--bottom" style="left:386px"></div>
  <div class="fold-mark fold-mark--bottom" style="left:813px"></div>
  <div class="fold-mark fold-mark--bottom" style="left:1006px"></div>

  <section class="sheet sheet--front">
    <article class="panel panel--welcome">
      <h2 class="panel-heading welcome-heading">Welcome to Reelside<br>Tides Bayvale!</h2>
      <div class="rule" style="top:60px; left:6px; right:0;"></div>
      <p class="body-copy welcome-copy">
        Cal Dunmore has<br>
        return from travelling and fishing<br>
        Australia, to start<br>
        Reelside Tides Bayvale.<br>
        Previous manager/operator<br>
        of Swiftline, High Ledge Tours.<br>
        We offer fully catered trips ranging<br>
        from 2 to 9 hours weather<br>
        fishing, diving, snorkeling,<br>
        whale watching, Corbett<br>
        Reef Nature Cruise, or a mix of all<br>
        our options. Specialising in<br>
        small groups from shared<br>
        charters to private with a<br>
        personalised service.<br>
        We use the latest top quality<br>
        gear available from<br>
        our fishing tackle, lures to electronics.<br>
        <br>
        Our boat is a 9.8 metre purpose<br>
        built fishing and tour boat,<br>
        with toilet and cooking facilities.<br>
        <br>
        We offer tea, coffee, soft drinks,<br>
        water, light refreshments<br>
        on all our charters/tours and lunch is<br>
        provided on a full day fishing charter.
      </p>
    </article>

    <article class="panel panel--fishing">
      <div class="rule" style="top:11px; left:7px; right:7px;"></div>
      <h2 class="panel-heading fishing-title">Fishing</h2>
      <div class="rule" style="top:62px; left:7px; right:7px;"></div>
      <p class="body-copy fishing-copy">
        Targeting: Tuna, Marlin, Kingfish,<br>
        Trumpeter, Blueeye Cod,<br>
        Hapaku, Sharks and all our<br>
        other local reef and deep water<br>
        fish, depending on the season and<br>
        charter and type of fishing you<br>
        are interested in.
      </p>
      <div class="photo" role="img" aria-label="Photo of the skipper on deck holding a large reef fish, open sea behind" style="top:159px; left:0; width:193px; height:176px;"></div>
      <p class="fishing-prices">
        5 Hour Fish<br>
        - $150 per person<br>
        9 Hour Fish<br>
        - $250 per person
      </p>
    </article>

    <article class="panel panel--cruises">
      <div class="rule" style="top:12px; left:5px; right:5px;"></div>
      <h2 class="panel-heading cruise-heading">Corbett Reef<br>Nature Cruises</h2>
      <div class="rule" style="top:61px; left:5px; right:5px;"></div>
      <h3 class="tour-title" style="top:86px;">Morning Tour 4 Hours 8:30am</h3>
      <p class="body-copy cruise-copy" style="top:108px;">
        Enjoy a 20 minute boat ride to Corbett<br>
        Reef, keeping an eye out for Dolphin,<br>
        whales and other wildlife, take a 1 hour<br>
        guided tour of Corbett Reef, return<br>
        to the boat for light<br>
        refreshment, then cruise along the shore line,<br>
        visiting the seal colonys, then enjoy your<br>
        journey home: $120 per person
      </p>
      <div class="rule" style="top:231px; left:5px; right:5px;"></div>
      <h3 class="tour-title" style="top:255px;">Afternoon Tour 3 Hours 12:30pm</h3>
      <p class="body-copy cruise-copy" style="top:277px;">
        Enjoy a 20 minute boat ride to the Reef,<br>
        keeping an eye out for dolphins, whales and<br>
        other wildlife along the way, arriving at the<br>
        reef to visit the seal colonys, then a short<br>
        cruise along the shore line, enjoying light<br>
        refreshments, then take a 2 1/2 hour<br>
        guided tour of the Reef. Return to<br>
        the boat for a cold drink and enjoy<br>
        your journey home: $100 per person
      </p>
      <div class="rule" style="top:398px; left:5px; right:5px;"></div>
    </article>
  </section>

  <section class="sheet sheet--back">
    <article class="panel panel--cover">
      <div class="rule" style="top:17px; left:7px; right:7px;"></div>
      <h1 class="panel-heading cover-title">Reelside<br>Tides<br>Bayvale</h1>
      <div class="rule" style="top:146px; left:7px; right:7px;"></div>
      <div class="photo" role="img" aria-label="Photo of the skipper on the boat holding two caught fish" style="top:161px; left:23px; width:148px; height:220px;"></div>
    </article>

    <article class="panel panel--blank"></article>

    <article class="panel panel--contact">
      <div class="rule" style="top:31px; left:6px; right:6px;"></div>
      <p class="contact-block" style="top:58px;">
        To Book or For More Information:<br>
        Call us on 0400 555 019<br>
        Email us at<br>
        cal@reelsidetidesbayvale.example
      </p>
      <div class="rule" style="top:127px; left:6px; right:6px;"></div>
      <p class="contact-block" style="top:167px;">
        For more details on any of our<br>
        services, visit our website:<br>
        <span style="display:block; margin-top:9px; font-size:10.5px;">www.reelsidetidesbayvale.example</span>
      </p>
      <div class="rule" style="top:243px; left:6px; right:6px;"></div>
      <p class="contact-block" style="top:272px;">
        Reelside Tides Bayvale<br>
        PO Box 204<br>
        Bayvale NSW 2999
      </p>
      <div class="rule" style="top:337px; left:6px; right:6px;"></div>
    </article>
  </section>
</body>
</html>
```